Skin Care Product Line needs custom designed labels

We need one to two label design templates that can be used across our natural skin care products such as body lotion, salt scrubs, lip balms, handmade soaps, body creams, body mists, foot creams, bath salts. The design will come in different colors. We have our own logo; however the logo should have the flower colored golden along with the word tisbel.
Label sizes are :
1) 6 inches by 4 inches rectangular for body lotion,
2) 81/2 inches by 2 inches rectangular for body scrub,
3) 5 inches by 3 inches rectangular for body mist,
4) 2 inches by 3 inches for bath salts,
5) 2.125 inches by 2.125 inches for lip balm,
6) 11/2 inches by 1/12 inches label for soap.

The design should have a beige background with one color or two of the same colors for instance light lavender and a darker lavender. It should have a vintage feel to it because it's for a natural skin care line not commercial type. Also the fonts should be vintage looking. We can have one design with different colors such as light green, light yellow, light pink, light blue , light orange to go with the different scents. Added Tuesday, January 26, 2016

Target Market(s)

Young adults and aging boomers

Industry/Entity Type

Skin Care Product

Font styles to use
Decorative

Colors
cfeae6
b7a5cd
e4daeb
fbf289
fac994
9bcb3b
f9d9e8
f04a50
f68d4c

Requirements
Must have
• Please see attached image for design sample. Original Label design should have beige to tan colored background similar to the attached file. light colors such as lavender, light yellow, light orange, etc can be changed once original label is designed. We would need to be able to edit label design text and label design colors to match our different scents after we decide on the design.

```html
<!DOCTYPE html>
<html lang="en">
<head>
<meta charset="utf-8">
<title>tisbel – Jojoba Facial Moisturizer Labels</title>
<link href="https://fonts.googleapis.com/css2?family=Quicksand:wght@500;600;700&display=swap" rel="stylesheet">
<style>
  :root {
    --page-bg: #f6f6f4;
    --ink: #3a3a3a;
    --ink-soft: #6b6b6b;
    --rule: #7a7a78;
    --lace: #c4c4c0;
    --medallion-ring: #a3a3a0;
    --medallion-face: #f8f8f5;
    --gold: #c9a227;
    --label-edge: #d2d2cc;
  }
  html, body {
    margin: 0;
    width: 1200px;
    height: 560px;
    overflow: hidden;
    background: var(--page-bg);
    font-family: "Quicksand", sans-serif;
  }
  .label-row {
    width: 1200px;
    height: 560px;
    display: flex;
    justify-content: center;
    align-items: center;
    gap: 40px;
  }
  .label {
    width: 240px;
    height: 330px;
    display: block;
  }
  .label--sage   { --top: #dde6d3; --band: #cddbbf; --bottom: #e9ede4; }
  .label--sky    { --top: #a8c7e0; --band: #ece6c8; --bottom: #eef0ec; }
  .label--pearl  { --top: #e4e4e6; --band: #dcdcdf; --bottom: #eeeeef; }

  .label__top     { fill: var(--top); }
  .label__bottom  { fill: var(--bottom); }
  .label__edge    { fill: none; stroke: var(--label-edge); stroke-width: 1; }
  .label__lace    { fill: var(--lace); }
  .label__band    { fill: var(--band); }
  .label__rule    { stroke: var(--rule); stroke-width: 0.8; }
  .medallion__ring { fill: var(--medallion-ring); }
  .medallion__face { fill: var(--medallion-face); }
  .medallion__flourish { fill: var(--medallion-ring); }

  .brand__dot   { fill: var(--gold); }
  .brand__name  { font-family: "Quicksand", sans-serif; font-weight: 600; font-size: 15px; fill: var(--ink-soft); }
  .brand__tagline { font-family: "Quicksand", sans-serif; font-weight: 500; font-size: 5.5px; letter-spacing: 0.4px; fill: var(--ink-soft); }
  .product__name { font-family: "Quicksand", sans-serif; font-weight: 700; font-size: 19px; fill: var(--ink); }
  .product__type { font-family: "Quicksand", sans-serif; font-weight: 500; font-size: 12.5px; letter-spacing: 2.4px; fill: var(--ink-soft); }
  .product__line { font-family: "Quicksand", sans-serif; font-weight: 500; font-size: 11px; letter-spacing: 0.5px; fill: var(--ink-soft); }
</style>
</head>
<body>
<main class="label-row">

  <svg class="label label--sage" viewBox="0 0 240 330" aria-label="Jojoba Facial Moisturizer label, sage">
    <defs><path id="arc-sage" d="M 50 196 A 70 70 0 0 0 190 196"/></defs>
    <rect class="label__top" x="0" y="0" width="240" height="165"/>
    <rect class="label__bottom" x="0" y="165" width="240" height="165"/>
    <rect class="label__lace" x="0" y="6" width="240" height="10" role="img" aria-label="lace border"/>
    <rect class="label__lace" x="0" y="314" width="240" height="10" role="img" aria-label="lace border"/>
    <circle class="medallion__ring" cx="120" cy="165" r="94" role="img" aria-label="scalloped medallion border"/>
    <circle class="medallion__face" cx="120" cy="165" r="84"/>
    <rect class="label__band" x="0" y="128" width="240" height="74"/>
    <line class="label__rule" x1="0" y1="128" x2="240" y2="128"/>
    <line class="label__rule" x1="0" y1="132" x2="240" y2="132"/>
    <line class="label__rule" x1="0" y1="198" x2="240" y2="198"/>
    <line class="label__rule" x1="0" y1="202" x2="240" y2="202"/>
    <circle class="brand__dot" cx="98" cy="100" r="5"/>
    <text class="brand__name" x="107" y="105">tisbel</text>
    <text class="brand__tagline" x="120" y="118" text-anchor="middle">Pure Botanical Care</text>
    <text class="product__name" x="120" y="167" text-anchor="middle">JOJOBA FACIAL</text>
    <text class="product__type" x="120" y="189" text-anchor="middle">MOISTURIZER</text>
    <rect class="medallion__flourish" x="106" y="210" width="28" height="7" role="img" aria-label="flourish ornament"/>
    <text class="product__line"><textPath href="#arc-sage" startOffset="50%" text-anchor="middle">Natural Products</textPath></text>
    <rect class="label__edge" x="0.5" y="0.5" width="239" height="329"/>
  </svg>

  <svg class="label label--sky" viewBox="0 0 240 330" aria-label="Jojoba Facial Moisturizer label, sky">
    <defs><path id="arc-sky" d="M 50 196 A 70 70 0 0 0 190 196"/></defs>
    <rect class="label__top" x="0" y="0" width="240" height="165"/>
    <rect class="label__bottom" x="0" y="165" width="240" height="165"/>
    <rect class="label__lace" x="0" y="6" width="240" height="10" role="img" aria-label="lace border"/>
    <rect class="label__lace" x="0" y="314" width="240" height="10" role="img" aria-label="lace border"/>
    <circle class="medallion__ring" cx="120" cy="165" r="94" role="img" aria-label="scalloped medallion border"/>
    <circle class="medallion__face" cx="120" cy="165" r="84"/>
    <rect class="label__band" x="0" y="128" width="240" height="74"/>
    <line class="label__rule" x1="0" y1="128" x2="240" y2="128"/>
    <line class="label__rule" x1="0" y1="132" x2="240" y2="132"/>
    <line class="label__rule" x1="0" y1="198" x2="240" y2="198"/>
    <line class="label__rule" x1="0" y1="202" x2="240" y2="202"/>
    <circle class="brand__dot" cx="98" cy="100" r="5"/>
    <text class="brand__name" x="107" y="105">tisbel</text>
    <text class="brand__tagline" x="120" y="118" text-anchor="middle">Pure Botanical Care</text>
    <text class="product__name" x="120" y="167" text-anchor="middle">JOJOBA FACIAL</text>
    <text class="product__type" x="120" y="189" text-anchor="middle">MOISTURIZER</text>
    <rect class="medallion__flourish" x="106" y="210" width="28" height="7" role="img" aria-label="flourish ornament"/>
    <text class="product__line"><textPath href="#arc-sky" startOffset="50%" text-anchor="middle">Natural Products</textPath></text>
    <rect class="label__edge" x="0.5" y="0.5" width="239" height="329"/>
  </svg>

  <svg class="label label--pearl" viewBox="0 0 240 330" aria-label="Jojoba Facial Moisturizer label, pearl">
    <defs><path id="arc-pearl" d="M 50 196 A 70 70 0 0 0 190 196"/></defs>
    <rect class="label__top" x="0" y="0" width="240" height="165"/>
    <rect class="label__bottom" x="0" y="165" width="240" height="165"/>
    <rect class="label__lace" x="0" y="6" width="240" height="10" role="img" aria-label="lace border"/>
    <rect class="label__lace" x="0" y="314" width="240" height="10" role="img" aria-label="lace border"/>
    <circle class="medallion__ring" cx="120" cy="165" r="94" role="img" aria-label="scalloped medallion border"/>
    <circle class="medallion__face" cx="120" cy="165" r="84"/>
    <rect class="label__band" x="0" y="128" width="240" height="74"/>
    <line class="label__rule" x1="0" y1="128" x2="240" y2="128"/>
    <line class="label__rule" x1="0" y1="132" x2="240" y2="132"/>
    <line class="label__rule" x1="0" y1="198" x2="240" y2="198"/>
    <line class="label__rule" x1="0" y1="202" x2="240" y2="202"/>
    <circle class="brand__dot" cx="98" cy="100" r="5"/>
    <text class="brand__name" x="107" y="105">tisbel</text>
    <text class="brand__tagline" x="120" y="118" text-anchor="middle">Pure Botanical Care</text>
    <text class="product__name" x="120" y="167" text-anchor="middle">JOJOBA FACIAL</text>
    <text class="product__type" x="120" y="189" text-anchor="middle">MOISTURIZER</text>
    <rect class="medallion__flourish" x="106" y="210" width="28" height="7" role="img" aria-label="flourish ornament"/>
    <text class="product__line"><textPath href="#arc-pearl" startOffset="50%" text-anchor="middle">Natural Products</textPath></text>
    <rect class="label__edge" x="0.5" y="0.5" width="239" height="329"/>
  </svg>

  <svg class="label label--sage" viewBox="0 0 240 330" aria-label="Jojoba Facial Moisturizer label, sage">
    <defs><path id="arc-sage-2" d="M 50 196 A 70 70 0 0 0 190 196"/></defs>
    <rect class="label__top" x="0" y="0" width="240" height="165"/>
    <rect class="label__bottom" x="0" y="165" width="240" height="165"/>
    <rect class="label__lace" x="0" y="6" width="240" height="10" role="img" aria-label="lace border"/>
    <rect class="label__lace" x="0" y="314" width="240" height="10" role="img" aria-label="lace border"/>
    <circle class="medallion__ring" cx="120" cy="165" r="94" role="img" aria-label="scalloped medallion border"/>
    <circle class="medallion__face" cx="120" cy="165" r="84"/>
    <rect class="label__band" x="0" y="128" width="240" height="74"/>
    <line class="label__rule" x1="0" y1="128" x2="240" y2="128"/>
    <line class="label__rule" x1="0" y1="132" x2="240" y2="132"/>
    <line class="label__rule" x1="0" y1="198" x2="240" y2="198"/>
    <line class="label__rule" x1="0" y1="202" x2="240" y2="202"/>
    <circle class="brand__dot" cx="98" cy="100" r="5"/>
    <text class="brand__name" x="107" y="105">tisbel</text>
    <text class="brand__tagline" x="120" y="118" text-anchor="middle">Pure Botanical Care</text>
    <text class="product__name" x="120" y="167" text-anchor="middle">JOJOBA FACIAL</text>
    <text class="product__type" x="120" y="189" text-anchor="middle">MOISTURIZER</text>
    <rect class="medallion__flourish" x="106" y="210" width="28" height="7" role="img" aria-label="flourish ornament"/>
    <text class="product__line"><textPath href="#arc-sage-2" startOffset="50%" text-anchor="middle">Natural Products</textPath></text>
    <rect class="label__edge" x="0.5" y="0.5" width="239" height="329"/>
  </svg>

</main>
</body>
</html>
```